Wordpress theme customised please - for new ecommerce homewares website

Hi, we need a wordpress theme customised for a business that will sell tea towels (aka kitchen towels/dish cloths).
We do not have a website currently, but wish to launch using wordpress + woocommerce + "the shopfront" theme (c/- plumkestrel).
BACKGROUND RE THE BUSINESS
Our products are very stylish and will appeal to people who like owning gorgeous things - people who love cooking and/or decorating their home beautifully, or maybe they like travelling and/or buying presents for themselves and friends/family etc.
As they are typically used in people's kitchens, so "fresh" and "clean" is important - however the site must look very upmarket: timeless yet current, and classic yet simple, but not pretty, fussy or edgy.
We believe we have a great opportunity to leverage the "feel" of the product - cotton & linen fabric that has real texture to it, is tactile, natural, raw, real... in the photos used on the website, the backgrounds etc
Our logo is attached - a very dark grey colour was chosen, with white stripes, so that its neutral colouring would coordinate well with our suppliers' existing packaging. (We will represent a number of brands.)
BACKGROUND RE THIS PROJECT
We already know we want to use "the shopfront" theme by plumkestrel, but we need help customising the look of this theme so it works well with our logo, looks really striking and doesn't look like everyone else's ie "straight out of the box".
It appears these are the types of things that can be changed:
LAYOUT:
home page design concept (eg with a cascade carousel)
page design concept for eg About Us, Contact Us, FAQs
landing page design concept
header; light footer; dark footer
COLOURS & BACKGROUNDS & BORDERS & SEPARATORS:
main theme colour; accent colour; primary font colour
header background; light footer background colour; dark footer background colour; copyright bar background colour
dark footer widget title border; dark footer list separators and borders; dark footer/copyright bar separator styles
FONTS:
main navigation text colour; secondary navigation text colour; dark footer text colour; copyright bar text colour
main font; secondary font
LASTLY
Please don't hesitate to ask questions, request further information etc This is the first time we've posted a design project like this so it's tricky to know what other information you will need, so please just get in touch, ok!
Thanks so much for your interest in this project, and best wishes.

```html
<!DOCTYPE html>
<html lang="en">
<head>
<meta charset="utf-8">
<title>Hearth &amp; Weave — Home</title>
<link href="https://fonts.googleapis.com/css2?family=Lato:wght@400;700&family=Oswald:wght@500&display=swap" rel="stylesheet">
<style>
:root{
  --page-bg:#141414;
  --white:#ffffff;
  --ink:#1f1f1f;
  --muted:#8a8a8a;
  --body-grey:#6b6b6b;
  --accent:#f7c815;
  --bar-dark:#3b3b3b;
  --panel:#e7e1df;
  --rule:#2a2a2a;
  --footer:#0b0e15;
  --footer-text:#ffffff;
  --star:#f2a51c;
  --star-empty:#ffffff;
  --frame:#dcdcdc;
}
*{box-sizing:border-box;margin:0;padding:0}
html,body{width:1200px;height:1035px;overflow:hidden}
body{background:var(--page-bg);font-family:'Lato',sans-serif;color:var(--ink);position:relative}
.page{position:absolute;left:35px;top:0;width:1129px;height:1035px}

/* Blog */
.blog{position:absolute;left:0;top:0;width:1129px;height:323px;background:var(--white)}
.blog-title{position:absolute;left:13px;top:9px;font-family:'Oswald',sans-serif;font-weight:500;font-size:28px;letter-spacing:.5px;color:var(--ink)}
.blog-nav{position:absolute;top:22px;width:29px;height:29px;background:#000;display:flex;align-items:center;justify-content:center}
.blog-nav.prev{left:1054px}.blog-nav.next{left:1086px}
.title-bar{position:absolute;left:13px;top:56px;width:1102px;height:7px;background:var(--accent)}
.title-bar::before{content:"";position:absolute;left:0;top:0;width:216px;height:7px;background:var(--bar-dark)}
.post{position:absolute;top:81px;width:460px;height:190px}
.post-thumb{position:absolute;left:0;top:0;width:232px;height:190px;border:1px solid var(--frame);background:#f1f1f1;padding:8px}
.post-thumb .fill{width:100%;height:100%;background:linear-gradient(160deg,#8ccbe0,#5fa9c6 55%,#7b6f6b)}
.post-heading{position:absolute;left:259px;top:4px;width:240px;font-size:19px;line-height:21px;font-weight:400;color:var(--ink)}
.post-meta{position:absolute;left:259px;top:51px;font-size:12.5px;color:var(--muted)}
.post-excerpt{position:absolute;left:259px;top:73px;width:225px;font-size:14.5px;line-height:18.5px;color:var(--body-grey)}
.read-more{position:absolute;left:259px;top:159px;width:91px;height:28px;background:var(--ink);color:var(--white);border-radius:3px;font-size:12px;display:flex;align-items:center;justify-content:center;letter-spacing:.2px}

/* Product lists */
.lists{position:absolute;left:0;top:323px;width:1129px;height:368px;background:var(--panel)}
.list{position:absolute;top:0;width:341px}
.list-title{position:absolute;left:2px;top:10px;font-size:14.5px;font-weight:700;text-transform:uppercase;color:var(--ink)}
.list-title::after{content:"";position:absolute;left:-2px;top:27px;width:341px;height:3px;background:var(--rule)}
.item{position:absolute;left:0;width:341px;height:104px}
.item + .item::before{content:"";position:absolute;left:0;top:-11px;width:341px;height:1px;background:#555}
.item-thumb{position:absolute;left:0;top:0;width:79px;height:81px}
.thumb-towel{background:linear-gradient(150deg,#7fc2dc,#4f97b6 60%,#6e6a68)}
.thumb-band{background:linear-gradient(180deg,#2e2620,#c9ccb5 45%,#e8e6e0 70%,#3a2f28)}
.thumb-face{background:linear-gradient(160deg,#e9c39c,#d79a78 55%,#6aa0b5)}
.item-name{position:absolute;left:90px;top:2px;width:250px;font-size:14.5px;line-height:18px;color:var(--ink)}
.item-price{position:absolute;left:90px;font-size:14.5px;font-weight:700;color:var(--ink)}
.item-by{position:absolute;left:94px;top:55px;font-size:14.5px;color:var(--ink)}
.stars{position:absolute;left:90px;top:26px;display:flex;gap:4px}

/* Footer */
.footer{position:absolute;left:0;top:701px;width:1129px;height:257px;background:var(--footer);color:var(--footer-text)}
.footer-col{position:absolute;top:30px}
.footer-heading{font-size:15px;font-weight:700;color:var(--accent);text-transform:uppercase;margin-bottom:14px}
.footer-about{width:262px;font-size:14px;line-height:19.5px}
.footer-links{list-style:none;font-size:14px;line-height:24.7px}
.social{display:grid;grid-template-columns:repeat(3,36px);gap:16px 15px;margin-top:18px;margin-left:-4px}
.social-item{width:36px;height:36px;border-radius:50%;background:var(--white);color:var(--footer);display:flex;align-items:center;justify-content:center;font-size:9px;font-weight:700}
.copyright-rule{position:absolute;left:0;top:958px;width:1129px;height:4px;background:var(--white)}
.copyright{position:absolute;left:0;top:962px;width:1129px;height:73px;background:var(--footer);color:var(--footer-text)}
.copyright-text{position:absolute;left:21px;top:30px;font-size:14px}
.secure{position:absolute;left:691px;top:32px;font-size:12px;font-weight:700;letter-spacing:.3px}
.cards{position:absolute;left:821px;top:22px;display:flex;gap:7px}
.card{width:51px;height:31px;background:var(--white);border-radius:3px;color:var(--footer);font-size:10px;font-weight:700;display:flex;align-items:center;justify-content:center}
</style>
</head>
<body>
<div class="page">

  <section class="blog">
    <h2 class="blog-title">FROMM THE BLOG</h2>
    <span class="blog-nav prev"><svg width="12" height="16" viewBox="0 0 12 16"><path d="M9 2 3 8l6 6" stroke="#fff" stroke-width="3" fill="none"/></svg></span>
    <span class="blog-nav next"><svg width="12" height="16" viewBox="0 0 12 16"><path d="M3 2l6 6-6 6" stroke="#fff" stroke-width="3" fill="none"/></svg></span>
    <div class="title-bar"></div>

    <article class="post" style="left:13px">
      <div class="post-thumb"><div class="fill" role="img" aria-label="Blue lattice-print hanging tea towel with a button on a grey knit towel"></div></div>
      <h3 class="post-heading">Lorem ipsum dolot sit amet esta di amria</h3>
      <p class="post-meta">7 comments</p>
      <p class="post-excerpt">Lorem ipsum dolor sit amet, consectetur adipiscing elit. Ut vel lacus nec tellus condimentum commodo.</p>
      <span class="read-more">READ MORE</span>
    </article>

    <article class="post" style="left:620px">
      <div class="post-thumb"><div class="fill" role="img" aria-label="Blue lattice-print hanging tea towel with a button on a grey knit towel"></div></div>
      <h3 class="post-heading">Lorem ipsum dolot sit amet esta di amria</h3>
      <p class="post-meta">7 comments</p>
      <p class="post-excerpt">Lorem ipsum dolor sit amet, consectetur adipiscing elit. Ut vel lacus nec tellus condimentum commodo.</p>
      <span class="read-more">READ MORE</span>
    </article>
  </section>

  <svg width="0" height="0" style="position:absolute">
    <defs>
      <symbol id="star" viewBox="0 0 24 24"><path d="M12 1.8l3.1 6.6 7.2.9-5.3 5 1.4 7.1L12 17.9l-6.4 3.5L7 14.3l-5.3-5 7.2-.9z"/></symbol>
    </defs>
  </svg>

  <section class="lists">
    <div class="list" style="left:17px">
      <h4 class="list-title">Best Sellers</h4>
      <div class="item" style="top:52px">
        <div class="item-thumb thumb-towel" role="img" aria-label="Blue lattice-print tea towel"></div>
        <p class="item-name">Sed mi ipsum, euismod ac ultrices eu, tincidunt ac erat.</p>
        <p class="item-price" style="top:39px">$56.95</p>
      </div>
      <div class="item" style="top:155px">
        <div class="item-thumb thumb-band" role="img" aria-label="White towel wrapped with a green beaded band"></div>
        <p class="item-name">Sed mi ipsum, euismod ac ultrices eu, tincidunt ac erat.</p>
        <p class="item-price" style="top:39px">$56.95</p>
      </div>
      <div class="item" style="top:258px">
        <div class="item-thumb thumb-towel" role="img" aria-label="Blue lattice-print tea towel"></div>
        <p class="item-name">Sed mi ipsum, euismod ac ultrices eu, tincidunt ac erat.</p>
        <p class="item-price" style="top:39px">$56.95</p>
      </div>
    </div>

    <div class="list" style="left:395px">
      <h4 class="list-title">Top Rated Products</h4>
      <div class="item" style="top:52px">
        <div class="item-thumb thumb-band" role="img" aria-label="White towel wrapped with a green beaded band"></div>
        <p class="item-name">Sed mi ipsum, euismod ac ultrices..</p>
        <div class="stars"><svg width="22" height="22" fill="var(--star)"><use href="#star"/></svg><svg width="22" height="22" fill="var(--star)"><use href="#star"/></svg><svg width="22" height="22" fill="var(--star-empty)"><use href="#star"/></svg><svg width="22" height="22" fill="var(--star-empty)"><use href="#star"/></svg><svg width="22" height="22" fill="var(--star-empty)"><use href="#star"/></svg></div>
        <p class="item-price" style="top:56px;left:94px">$56.95</p>
      </div>
      <div class="item" style="top:155px">
        <div class="item-thumb thumb-towel" role="img" aria-label="Blue lattice-print tea towel"></div>
        <p class="item-name">Sed mi ipsum, euismod ac ultrices..</p>
        <div class="stars"><svg width="22" height="22" fill="var(--star)"><use href="#star"/></svg><svg width="22" height="22" fill="var(--star)"><use href="#star"/></svg><svg width="22" height="22" fill="var(--star-empty)"><use href="#star"/></svg><svg width="22" height="22" fill="var(--star-empty)"><use href="#star"/></svg><svg width="22" height="22" fill="var(--star-empty)"><use href="#star"/></svg></div>
        <p class="item-price" style="top:56px;left:94px">$56.95</p>
      </div>
      <div class="item" style="top:258px">
        <div class="item-thumb thumb-band" role="img" aria-label="White towel wrapped with a green beaded band"></div>
        <p class="item-name">Sed mi ipsum, euismod ac ultrices..</p>
        <div class="stars"><svg width="22" height="22" fill="var(--star)"><use href="#star"/></svg><svg width="22" height="22" fill="var(--star)"><use href="#star"/></svg><svg width="22" height="22" fill="var(--star-empty)"><use href="#star"/></svg><svg width="22" height="22" fill="var(--star-empty)"><use href="#star"/></svg><svg width="22" height="22" fill="var(--star-empty)"><use href="#star"/></svg></div>
        <p class="item-price" style="top:56px;left:94px">$56.95</p>
      </div>
    </div>

    <div class="list" style="left:774px">
      <h4 class="list-title">Recent Reviews</h4>
      <div class="item" style="top:52px">
        <div class="item-thumb thumb-face" role="img" aria-label="Portrait photo of the reviewer"></div>
        <p class="item-name">Sed mi ipsum, euismod ac ultrices..</p>
        <div class="stars"><svg width="22" height="22" fill="var(--star)"><use href="#star"/></svg><svg width="22" height="22" fill="var(--star)"><use href="#star"/></svg><svg width="22" height="22" fill="var(--star-empty)"><use href="#star"/></svg><svg width="22" height="22" fill="var(--star-empty)"><use href="#star"/></svg><svg width="22" height="22" fill="var(--star-empty)"><use href="#star"/></svg></div>
        <p class="item-by">By Miles</p>
      </div>
      <div class="item" style="top:155px">
        <div class="item-thumb thumb-face" role="img" aria-label="Portrait photo of the reviewer"></div>
        <p class="item-name">Sed mi ipsum, euismod ac ultrices..</p>
        <div class="stars"><svg width="22" height="22" fill="var(--star)"><use href="#star"/></svg><svg width="22" height="22" fill="var(--star)"><use href="#star"/></svg><svg width="22" height="22" fill="var(--star-empty)"><use href="#star"/></svg><svg width="22" height="22" fill="var(--star-empty)"><use href="#star"/></svg><svg width="22" height="22" fill="var(--star-empty)"><use href="#star"/></svg></div>
        <p class="item-by">By Owen</p>
      </div>
      <div class="item" style="top:258px">
        <div class="item-thumb thumb-face" role="img" aria-label="Portrait photo of the reviewer"></div>
        <p class="item-name">Sed mi ipsum, euismod ac ultrices..</p>
        <div class="stars"><svg width="22" height="22" fill="var(--star)"><use href="#star"/></svg><svg width="22" height="22" fill="var(--star)"><use href="#star"/></svg><svg width="22" height="22" fill="var(--star-empty)"><use href="#star"/></svg><svg width="22" height="22" fill="var(--star-empty)"><use href="#star"/></svg><svg width="22" height="22" fill="var(--star-empty)"><use href="#star"/></svg></div>
        <p class="item-by">By Nora</p>
      </div>
    </div>
  </section>

  <footer class="footer">
    <div class="footer-col" style="left:15px">
      <h5 class="footer-heading">About Hearth &amp; Weave</h5>
      <p class="footer-about">Lorem ipsum dolor sit amet, consectetur adipiscing elit. Nam sit amet tincidunt elit. Donec tempus commodo purus ac eleifend. Nulla euismod in felis eget suscipit. Sed non dui vitae orci vestibulum eleifend gravida quis orci. Mauris quis est dui. Nunc ac porta nisi. Proin erat eros.</p>
    </div>
    <div class="footer-col" style="left:357px">
      <h5 class="footer-heading">Home</h5>
      <ul class="footer-links"><li>Home</li><li>About Us</li><li>Company History</li><li>Services</li><li>Location Contact</li></ul>
    </div>
    <div class="footer-col" style="left:541px">
      <h5 class="footer-heading">Sell &amp; Service</h5>
      <ul class="footer-links"><li>Track Orders</li><li>Customer Care</li><li>My Account</li><li>Terms &amp; Conditions</li><li>Privacy</li></ul>
    </div>
    <div class="footer-col" style="left:748px">
      <h5 class="footer-heading">Misc.</h5>
      <ul class="footer-links"><li>Blog</li><li>Registration</li><li>Newsletter</li><li>Special Offers</li></ul>
    </div>
    <div class="footer-col" style="left:915px">
      <h5 class="footer-heading">Connect With Us</h5>
      <div class="social">
        <span class="social-item">Kith</span>
        <span class="social-item">Pinly</span>
        <span class="social-item"><svg width="16" height="12" viewBox="0 0 16 12"><rect width="16" height="12" rx="2" fill="#0b0e15"/><path d="M1 1l7 6 7-6" stroke="#fff" stroke-width="1.4" fill="none"/></svg></span>
        <span class="social-item">Chirp</span>
        <span class="social-item"><svg width="14" height="18" viewBox="0 0 14 18"><path d="M7 0a7 7 0 0 0-7 7c0 5 7 11 7 11s7-6 7-11a7 7 0 0 0-7-7z" fill="#0b0e15"/><circle cx="7" cy="7" r="2.6" fill="#fff"/></svg></span>
        <span class="social-item"><svg width="16" height="16" viewBox="0 0 24 24"><path d="M6.6 10.8a15.2 15.2 0 0 0 6.6 6.6l2.2-2.2c.3-.3.7-.4 1-.2 1.1.4 2.3.6 3.6.6.6 0 1 .4 1 1V20c0 .6-.4 1-1 1A17 17 0 0 1 3 4c0-.6.4-1 1-1h3.5c.6 0 1 .4 1 1 0 1.3.2 2.5.6 3.6.1.3 0 .7-.2 1z" fill="#0b0e15"/></svg></span>
      </div>
    </div>
  </footer>

  <div class="copyright-rule"></div>
  <div class="copyright">
    <p class="copyright-text">© 2013, All Rights Reserved, Hearth &amp; Weave</p>
    <p class="secure">SECURE PAYMENT</p>
    <div class="cards">
      <span class="card">Ferrow</span>
      <span class="card">Coinpath</span>
      <span class="card">Duoset</span>
      <span class="card">Farline</span>
      <span class="card">Riverly</span>
    </div>
  </div>

</div>
</body>
</html>
```